HVAC&INSULATION Company. Need a website INSULATION targeted.

We are a new HVAC and Insulation company from Washington. (less then 1 year). we already have a website, design, logo etc.. our existing website is targeted for HVAC services.

*** I want to open a 2nd website with a similar design. same logo. same name almost (ORVA INSULATION->ORVA INSULATION)

- our current website is www.orvacleangust.com
i want the new website to be targeted for insulation services

```html
<!DOCTYPE html>
<html lang="en">
<head>
<meta charset="utf-8">
<title>ORVA INSULATION – Insulation Installations</title>
<link href="https://fonts.googleapis.com/css2?family=Lato:wght@400;700;900&family=Roboto:wght@400;500;700&display=swap" rel="stylesheet">
<style>
:root{
  --blue:#1a8fe0;
  --blue-dark:#1478c4;
  --ink:#222222;
  --text:#555555;
  --white:#ffffff;
  --dark:#262626;
  --darker:#1c1c1c;
  --brown:#5a4a3c;
  --hero-a:#6b5a48;
  --hero-b:#a88f6e;
}
*{box-sizing:border-box;margin:0;padding:0}
html,body{width:1200px;height:2956px;overflow:hidden}
body{font-family:"Roboto",Arial,sans-serif;color:var(--text);background:var(--white);position:relative}
.wrap{position:relative;width:1200px}
a{color:inherit;text-decoration:none}
.btn{display:inline-flex;align-items:center;gap:8px;background:var(--blue);color:var(--white);font-family:"Roboto",sans-serif;font-weight:700;font-size:15px;text-transform:uppercase;border-radius:24px;padding:0 26px;height:48px;white-space:nowrap}
.btn .arrow{width:16px;height:16px;border-radius:50%;background:var(--white);display:inline-flex;align-items:center;justify-content:center}

/* hero */
.hero{position:relative;height:660px;overflow:hidden}
.hero-photo{position:absolute;inset:0;background:linear-gradient(115deg,#4a3e33 0%,var(--hero-a) 35%,var(--hero-b) 65%,#d8cdb8 100%)}
.hero-shade{position:absolute;inset:0;background:linear-gradient(90deg,rgba(0,0,0,.35),rgba(0,0,0,0) 60%)}
.logo{position:absolute;left:102px;top:22px;width:200px;text-align:center;color:var(--white)}
.logo-mark{width:88px;height:88px;border-radius:50%;background:var(--white);margin:0 auto 10px}
.logo-name{font-family:"Lato",sans-serif;font-weight:400;font-size:18px;letter-spacing:.5px;white-space:nowrap}
.top-row{position:absolute;right:112px;top:27px;display:flex;align-items:center;gap:18px}
.social-dot{width:16px;height:16px;border-radius:50%;background:var(--white)}
.top-row .btn{height:34px;font-size:15px;padding:0 26px;margin-left:16px}
.nav-rule{position:absolute;left:340px;right:112px;top:87px;height:1px;background:rgba(255,255,255,.7)}
.nav{position:absolute;right:112px;top:114px;display:flex;gap:24px;color:var(--white);font-weight:500;font-size:15px;text-transform:uppercase;white-space:nowrap}
.hero-title{position:absolute;left:108px;top:252px;color:var(--white);font-family:"Lato",sans-serif;font-weight:700;font-size:45px;line-height:56px;letter-spacing:5px;text-transform:uppercase}
.hero .cta{position:absolute;left:110px;top:396px}
.badges{position:absolute;left:110px;top:482px;display:flex;gap:14px;align-items:center}
.badge{background:rgba(255,255,255,.9)}
.badge.round{width:48px;height:48px;border-radius:50%}
.badge.rect{width:72px;height:40px;border-radius:4px}
.badge.wide{width:80px;height:36px;border-radius:4px}
.badge.sq{width:38px;height:38px;border-radius:6px;background:#3d6fd0}

/* services */
.services{position:relative;height:272px;background:var(--blue)}
.notch{position:absolute;left:550px;top:-60px}
.service-row{position:absolute;left:95px;right:95px;top:92px;display:flex;justify-content:space-between}
.service{width:180px;text-align:center;color:var(--white);font-family:"Roboto",sans-serif;font-weight:700;font-size:18px;text-transform:uppercase;white-space:nowrap}
.service svg{display:block;margin:0 auto 16px}
.chev{position:absolute;top:136px}

/* who we are */
.about{position:relative;height:528px}
.about h2{position:absolute;left:110px;top:100px;font-family:"Lato",sans-serif;font-weight:700;font-size:37px;color:var(--ink);text-transform:uppercase}
.about .copy{position:absolute;left:110px;top:176px;width:492px;font-size:13px;line-height:26px}
.about .copy p+p{margin-top:26px}
.about .btn{position:absolute;left:110px;top:366px}
.about-photo{position:absolute;left:632px;top:110px;width:456px;height:304px;background:linear-gradient(135deg,#8c6a52,#4a3528 60%,#2f4a2e)}

/* quote band */
.quote{position:relative;height:351px;background:linear-gradient(90deg,var(--darker),#303030 50%,var(--darker));text-align:center;color:var(--white)}
.quote h2{padding-top:80px;font-family:"Lato",sans-serif;font-weight:700;font-size:35px;line-height:52px;text-transform:uppercase}
.quote .btn{margin-top:54px;height:46px;padding:0 30px}

/* insulation */
.insulation{position:relative;height:432px}
.ins-photo{position:absolute;left:0;top:0;width:600px;height:432px;background:linear-gradient(135deg,#c99564,#7a5232 55%,#3a2a20)}
.insulation h2{position:absolute;left:676px;top:58px;font-family:"Lato",sans-serif;font-weight:700;font-size:37px;color:var(--ink);text-transform:uppercase}
.insulation .copy{position:absolute;left:676px;top:126px;width:412px;font-size:13px;line-height:24px;text-align:justify}
.insulation .copy p+p{margin-top:16px}
.insulation .btn{position:absolute;left:676px;top:318px}

/* help band */
.help{position:relative;height:246px;background:linear-gradient(90deg,var(--blue),#2a9bea 60%,var(--blue-dark));color:var(--white)}
.help h2{position:absolute;left:110px;top:66px;font-family:"Lato",sans-serif;font-weight:700;font-size:35px;text-transform:uppercase}
.help p{position:absolute;left:110px;top:124px;font-size:14.5px}
.help .btn{position:absolute;left:880px;top:88px;background:var(--brown);height:48px;padding:0 38px}

/* footer */
.footer{position:relative;height:467px;background:var(--dark);color:var(--white)}
.footer h3{font-family:"Roboto",sans-serif;font-weight:700;font-size:18px;text-transform:uppercase;text-decoration:underline;text-underline-offset:5px}
.col{position:absolute;top:104px}
.links{left:110px}
.links ul{list-style:none;margin-top:30px}
.links li{font-size:14px;line-height:30px;display:flex;align-items:center;gap:20px}
.links li::before{content:"»";font-weight:700}
.contact{left:336px}
.contact .row{display:flex;gap:24px;margin-top:32px;font-size:14px;line-height:22px}
.contact .row svg{flex:none;margin-top:2px}
.contact .row:first-of-type{margin-top:34px}
.form{left:654px;width:434px}
.form p{margin-top:28px;font-size:13px;line-height:22px}
.fields{margin-top:28px;display:grid;grid-template-columns:208px 208px;gap:18px}
.field{height:44px;border:1px solid #bbb;font-size:12px;padding:0 14px;display:flex;align-items:center}
.submit{height:44px;background:var(--blue);display:flex;align-items:center;justify-content:center;font-weight:700;font-size:17px;text-transform:uppercase}
.foot-rule{position:absolute;left:110px;right:112px;top:380px;height:1px;background:rgba(255,255,255,.5)}
.copyright{position:absolute;left:110px;top:418px;font-size:14px}
.foot-social{position:absolute;right:112px;top:408px;display:flex;gap:8px}
.foot-social span{width:30px;height:30px;border:1.5px solid var(--white);border-radius:50%}
</style>
</head>
<body>
<div class="wrap">

<header class="hero">
  <div class="hero-photo" role="img" aria-label="Installer in a plaid shirt and cap fitting insulation batts between the rafters of an attic with a skylight"></div>
  <div class="hero-shade"></div>
  <div class="logo">
    <div class="logo-mark"></div>
    <div class="logo-name">ORVA INSULATION</div>
  </div>
  <div class="top-row">
    <span class="social-dot"></span><span class="social-dot"></span><span class="social-dot"></span><span class="social-dot"></span><span class="social-dot"></span><span class="social-dot"></span><span class="social-dot"></span>
    <a class="btn" href="#">Get a Quote</a>
  </div>
  <div class="nav-rule"></div>
  <nav class="nav">
    <a href="#">Home</a><a href="#">Our Team</a><a href="#">Our Services</a><a href="#">Our Reviews</a><a href="#">Savings &amp; Specials</a><a href="#">Contact</a>
  </nav>
  <h1 class="hero-title">Insulation<br>Installations</h1>
  <a class="btn cta" href="#">Get a Free Quote <span class="arrow"><svg width="10" height="10" viewBox="0 0 10 10"><path d="M3 2l3 3-3 3" fill="none" stroke="#1a8fe0" stroke-width="2"/></svg></span></a>
  <div class="badges">
    <span class="badge round"></span><span class="badge rect"></span><span class="badge wide"></span><span class="badge wide"></span><span class="badge sq"></span>
  </div>
</header>

<section class="services">
  <svg class="notch" width="100" height="120" viewBox="0 0 100 120">
    <path d="M0 60 L50 10 L100 60 Z" fill="#1a8fe0"/>
    <rect x="38" y="28" width="24" height="38" rx="12" fill="none" stroke="#fff" stroke-width="2.5"/>
    <line x1="50" y1="36" x2="50" y2="44" stroke="#fff" stroke-width="2.5"/>
    <path d="M50 74v16M44 84l6 6 6-6" fill="none" stroke="#fff" stroke-width="2.5"/>
  </svg>
  <svg class="chev" style="left:44px" width="20" height="30" viewBox="0 0 20 30"><path d="M15 4 5 15l10 11" fill="none" stroke="#fff" stroke-width="3"/></svg>
  <svg class="chev" style="right:44px" width="20" height="30" viewBox="0 0 20 30"><path d="M5 4l10 11L5 26" fill="none" stroke="#fff" stroke-width="3"/></svg>
  <div class="service-row">
    <div class="service"><svg width="64" height="64" viewBox="0 0 64 64" fill="none" stroke="#fff" stroke-width="2"><rect x="6" y="6" width="52" height="52" rx="3"/><rect x="12" y="12" width="40" height="28"/><path d="M12 18h40M12 24h40M12 30h40M12 36h40"/><rect x="20" y="46" width="24" height="6"/></svg>Room Heating</div>
    <div class="service"><svg width="64" height="64" viewBox="0 0 64 64" fill="none" stroke="#fff" stroke-width="2"><path d="M8 14h26v12H8zM34 20h12a6 6 0 0 1 6 6v30M40 26v30M8 34h18M14 8v6M22 8v6"/></svg>Air Duct</div>
    <div class="service"><svg width="64" height="64" viewBox="0 0 64 64" fill="none" stroke="#fff" stroke-width="2"><rect x="8" y="28" width="22" height="30" rx="3"/><circle cx="19" cy="44" r="7"/><rect x="34" y="22" width="22" height="36" rx="3"/><circle cx="45" cy="42" r="7"/><path d="M19 28V12a8 8 0 0 1 16 0v10"/></svg>Dryer Vent</div>
    <div class="service"><svg width="64" height="64" viewBox="0 0 64 64" fill="none" stroke="#fff" stroke-width="2"><rect x="4" y="10" width="56" height="22" rx="3"/><path d="M10 24h44M12 38l-4 14M22 38l-2 16M32 38v18M42 38l2 16M52 38l4 14"/></svg>Air Conditioner</div>
    <div class="service"><svg width="64" height="64" viewBox="0 0 64 64" fill="none" stroke="#fff" stroke-width="2"><circle cx="32" cy="32" r="26"/><circle cx="32" cy="32" r="19"/><circle cx="32" cy="32" r="12"/><circle cx="32" cy="32" r="5"/><path d="M58 32h4"/></svg>Insulation</div>
  </div>
</section>

<section class="about">
  <h2>Who We Are</h2>
  <div class="copy">
    <p>ORVA INSULATION is a local and family owned company. We provide high quality insulation services with excellent customer satisfaction in the Everett, WA area.</p>
    <p>We help families keep their homes warm, improve their comfort and reduce their energy bills. We're committed to being a company and service that you trust. That is why we offer a 100% satisfaction guarantee on every project!</p>
  </div>
  <a class="btn" href="#">Read More <span class="arrow"><svg width="10" height="10" viewBox="0 0 10 10"><path d="M3 2l3 3-3 3" fill="none" stroke="#1a8fe0" stroke-width="2"/></svg></span></a>
  <div class="about-photo" role="img" aria-label="Person vacuuming a wooden floor beside a decorated holiday tree in a living room"></div>
</section>

<section class="quote">
  <h2>Get a Quote Fast<br>We Respond Within 24 Hours</h2>
  <a class="btn" href="#">Get Started <span class="arrow"><svg width="10" height="10" viewBox="0 0 10 10"><path d="M3 2l3 3-3 3" fill="none" stroke="#1a8fe0" stroke-width="2"/></svg></span></a>
</section>

<section class="insulation">
  <div class="ins-photo" role="img" aria-label="Worker in a white protective suit and mask placing an insulation board under wooden attic beams"></div>
  <h2>Insulation</h2>
  <div class="copy">
    <p>Lorem ipsum dolor sit amet, consectetur adipiscing elit, sed do eiusmod tempor incididunt ut labore et dolore magna aliqua.</p>
    <p>Ut enim ad minim veniam, quis nostrud exercitation ullamco laboris nisi ut aliquip ex ea commodo consequat. Duis aute irure dolor in reprehenderit in voluptate velit esse cillum dolore eu fugiat nulla pariatur sint occaecat cupidatat non proident.</p>
  </div>
  <a class="btn" href="#">Get Started <span class="arrow"><svg width="10" height="10" viewBox="0 0 10 10"><path d="M3 2l3 3-3 3" fill="none" stroke="#1a8fe0" stroke-width="2"/></svg></span></a>
</section>

<section class="help">
  <h2>How Can We Help You?</h2>
  <p>We respond to all feedback and inquiries and we look forward to hearing from you!</p>
  <a class="btn" href="#">Get a Quote <span class="arrow"><svg width="10" height="10" viewBox="0 0 10 10"><path d="M3 2l3 3-3 3" fill="none" stroke="#5a4a3c" stroke-width="2"/></svg></span></a>
</section>

<footer class="footer">
  <div class="col links">
    <h3>Quick Links</h3>
    <ul><li>Home</li><li>Our Team</li><li>Our Services</li><li>Our Reviews</li><li>Saving &amp; Specials</li><li>Contact Us</li></ul>
  </div>
  <div class="col contact">
    <h3>Contact Details</h3>
    <div class="row"><svg width="16" height="20" viewBox="0 0 16 20" fill="none" stroke="#fff" stroke-width="1.5"><path d="M8 19s6-6.5 6-11A6 6 0 0 0 2 8c0 4.5 6 11 6 11z"/><circle cx="8" cy="8" r="2"/></svg><span>123A, Sample Street, Sample<br>City, New State.</span></div>
    <div class="row"><svg width="16" height="16" viewBox="0 0 16 16" fill="none" stroke="#fff" stroke-width="1.5"><path d="M3 1h3l1.5 4-2 1.5a9 9 0 0 0 4 4L11 8.5l4 1.5v3a2 2 0 0 1-2 2A12 12 0 0 1 1 3a2 2 0 0 1 2-2z"/></svg><span>(555) 014-2876</span></div>
    <div class="row"><svg width="16" height="14" viewBox="0 0 16 14" fill="none" stroke="#fff" stroke-width="1.5"><rect x="1" y="1" width="14" height="12"/><path d="M1 1l7 6 7-6"/></svg><span>hello@orvainsulation.com</span></div>
  </div>
  <div class="col form">
    <h3>Contact Form</h3>
    <p>Lorem ipsum dolor sit amet, consectetur adipiscing elit, sed do eiusmod tempor incididunt ut labore...</p>
    <div class="fields">
      <div class="field">Name</div><div class="field">Email</div>
      <div class="field">Phone No</div><div class="submit">Submit</div>
    </div>
  </div>
  <div class="foot-rule"></div>
  <div class="copyright">Copyrights © 2018 ORVA INSULATION. All Rights Reserved &nbsp; | &nbsp; Privacy Policy.</div>
  <div class="foot-social"><span></span><span></span><span></span><span></span></div>
</footer>

</div>
</body>
</html>
```